Haldor Snekker AS
Buiness cards for haldor snekker as
Haldor Snekker AS - Construction
Creative Brief
Simple
Tobias Kranveldt
CEO
Lerkeskogveien 14 0587 OSLO Norway
post@haldorsnekker.example
www.haldorsnekker.example
Org. nr.: 836 402 517
Its for a company that expanse fast within big building sites
come up with something!?! we make your investment possible

```html
<!DOCTYPE html>
<html lang="no">
<head>
<meta charset="utf-8">
<title>Haldor Snekker AS – Visittkort</title>
<link href="https://fonts.googleapis.com/css2?family=Open+Sans:wght@400;600;700&display=swap" rel="stylesheet">
<style>
  :root {
    --backdrop: #3a3b3d;
    --card: #ffffff;
    --navy: #1f4677;
    --navy-dark: #173a63;
    --ink: #4a4a4a;
    --muted: #6b6b6b;
    --rule: #c9c9c9;
  }
  * { box-sizing: border-box; margin: 0; padding: 0; }
  html, body { width: 1200px; height: 852px; overflow: hidden; }
  body {
    background: var(--backdrop);
    font-family: "Open Sans", Arial, sans-serif;
    position: relative;
  }
  .card {
    position: absolute;
    width: 520px;
    height: 300px;
    background: var(--card);
    border-radius: 14px;
    overflow: hidden;
    box-shadow: 0 10px 28px rgba(0,0,0,.35);
  }
  .card::before {
    content: "";
    position: absolute;
    left: 0; top: 0; bottom: 0;
    width: 16px;
    background: linear-gradient(to bottom, var(--navy), var(--navy-dark));
  }
  .card--side { left: 60px; top: 90px; }
  .card--stacked { left: 620px; top: 462px; }

  .brand {
    display: flex;
    align-items: center;
    gap: 10px;
    color: var(--navy);
    font-weight: 700;
    font-size: 24px;
    letter-spacing: .5px;
    white-space: nowrap;
  }
  .brand__mark {
    width: 30px; height: 30px;
    background: var(--navy);
    flex: none;
  }

  .person__name { color: var(--navy); font-weight: 700; font-size: 17px; }
  .person__role { color: var(--ink); font-size: 12px; margin-top: 3px; }
  .address { color: var(--ink); font-size: 12px; line-height: 1.5; }
  .contacts { list-style: none; color: var(--ink); font-size: 12px; line-height: 1.75; }
  .contacts li { display: flex; align-items: center; gap: 8px; }
  .contacts svg { width: 12px; height: 12px; fill: var(--navy); flex: none; }
  .divider { position: absolute; width: 1px; background: var(--rule); }

  /* Card with logo left, details right */
  .card--side .brand { position: absolute; left: 44px; top: 128px; font-size: 20px; }
  .card--side .divider { left: 268px; top: 50px; height: 200px; }
  .card--side .details { position: absolute; left: 288px; top: 46px; }
  .card--side .address { margin-top: 16px; }
  .card--side .contacts { margin-top: 6px; }

  /* Card with logo top, split details */
  .card--stacked .brand { position: absolute; left: 140px; top: 52px; }
  .card--stacked .identity { position: absolute; right: 278px; top: 150px; text-align: right; }
  .card--stacked .address { margin-top: 14px; }
  .card--stacked .divider { left: 258px; top: 146px; height: 118px; }
  .card--stacked .contacts { position: absolute; left: 274px; top: 142px; }
</style>
</head>
<body>

<svg width="0" height="0" style="position:absolute">
  <defs>
    <symbol id="i-phone" viewBox="0 0 12 12"><rect x="3" y="0.5" width="6" height="11" rx="1.2"/><rect x="4.2" y="1.8" width="3.6" height="7" fill="#fff"/></symbol>
    <symbol id="i-fax" viewBox="0 0 12 12"><rect x="3" y="0.5" width="6" height="4"/><rect x="0.5" y="4" width="11" height="5" rx="1"/><rect x="3" y="7.5" width="6" height="4" fill="#fff" stroke="#1f4677"/></symbol>
    <symbol id="i-mail" viewBox="0 0 12 12"><rect x="0.5" y="2" width="11" height="8" rx="1"/><path d="M1 2.5 6 6.5 11 2.5" stroke="#fff" fill="none"/></symbol>
    <symbol id="i-web" viewBox="0 0 12 12"><circle cx="6" cy="6" r="5.5"/><path d="M0.5 6h11M6 0.5c-2.5 3-2.5 8 0 11M6 0.5c2.5 3 2.5 8 0 11" stroke="#fff" fill="none" stroke-width=".8"/></symbol>
  </defs>
</svg>

<article class="card card--side">
  <div class="brand"><span class="brand__mark"></span>Haldor Snekker</div>
  <span class="divider"></span>
  <div class="details">
    <p class="person__name">Tobias Kranveldt</p>
    <p class="person__role">CEO</p>
    <p class="address">Lerkeskogveien 14<br>0587 OSLO, Norway<br>Lin: 836 402 517</p>
    <ul class="contacts">
      <li><svg><use href="#i-phone"/></svg>+47 4120 5583</li>
      <li><svg><use href="#i-fax"/></svg>+47 2290 1146</li>
      <li><svg><use href="#i-mail"/></svg>post@haldorsnekker.example</li>
      <li><svg><use href="#i-web"/></svg>www.haldorsnekker.example</li>
    </ul>
  </div>
</article>

<article class="card card--stacked">
  <div class="brand"><span class="brand__mark"></span>Haldor Snekker</div>
  <div class="identity">
    <p class="person__name">Tobias Kranveldt</p>
    <p class="person__role">CEO</p>
    <p class="address">Lerkeskogveien 14<br>0587 OSLO, Norway</p>
  </div>
  <span class="divider"></span>
  <ul class="contacts">
    <li>Lin: 836 402 517</li>
    <li><svg><use href="#i-phone"/></svg>+47 4120 5583</li>
    <li><svg><use href="#i-fax"/></svg>+47 2290 1146</li>
    <li><svg><use href="#i-mail"/></svg>post@haldorsnekker.example</li>
    <li><svg><use href="#i-web"/></svg>www.haldorsnekker.example</li>
  </ul>
</article>

</body>
</html>
```